Burrow Chair

A5 Double Sided card for Chair Marketing
This will be our major marketing piece on a stiff piece fo cardboard
Dont feel the need to use all the words below "a picture tells the story" we can trim the words and make sure the message gets out
High end project
Feel free to use the word "burrow Chair" innovatively to give it some identity
Want it professional and you can use any of the photos as you see fit
mix up the words etc
• Upholstered in Italian Leather
• High Quality Merino Wool Sheepskins .
• 360 Degree rotation
• Handmade with love and detail
• Cosy
• Calming and unbelievably quiet acoustics
• Unique
This chair is unique and a labor of love and attention to detail, it’s a conversation starter or statement piece. It’s something you just can’t find anywhere.
The acoustics let you escape in any room whether you want to read a book or simply relax
The Dome or Halo chair
When Tapio Lindqvist had the first idea for the Dome Chair
in 1963, fibreglass was a relatively new material as glass reinforced products were not Batch Produced as they are today. The only possibility was to craft the chair with his own hands. It took Tapio and his brother in law nearly one year until the first prototype was ready.
The prototype was a success, it is still standing in Tapios house. By coincidence two young product managers from the company VELNO discovered the Dome Chair when visiting Tapio in order to look at some pine wood chairs. They immediately realised the potential of this design icon.
In 1966 for the first time the chair was presented at the Northern Interiors Expo in Cologne. Celebrities bought copies of the original for their homes and it found itself in a variety of Design Museums throughout the world.
The design of the chair was not only striking to look at but it was also comfortable and relaxing to sit in for long periods of time. The chair has been described as ''a room within a room''. It offers shelter, a calming atmosphere and privacy for the seated person.
Our Replica Tapio Lindqvist Dome chair is made to exacting standards. The shell is made from solid fiberglass, and is finished in Italian leather. The interior of the ball is padded and covered in lambswool merino sheepskins. The chair is available in different colours.
Feel free to photo shop the chair in front of a lifestyle scene ie an ope fireplace or modern room for a dynamic feel on the front side of the card
Contact details
Tie in the logo loaded as well
We are a small Australian Family creating unique products
TRV
Property of TRV Exports we love to create comfortable and unique things which people talk about and want to adorn their living spaces with.
We hope you love this product as much as we do and have many years enjoyment in it
Please order on our web site www.trvexports-example.com.au or email sales@trvexp-example.com.au
Mira Doyle
Marketing and Sales Manager
0491 203 417
Melbourne, Australia
Niche Market , for private and hotels and high end businesses

```html
<!DOCTYPE html>
<html lang="en">
<head>
<meta charset="utf-8">
<title>Burrow Chair – A5 Card</title>
<link href="https://fonts.googleapis.com/css2?family=Quicksand:wght@700&family=Patrick+Hand&family=Open+Sans:wght@400;600&display=swap" rel="stylesheet">
<style>
  :root {
    --backdrop: #a8a8a8;
    --sky-light: #e9f6ff;
    --sky: #c4e5fb;
    --gold: #c99a1e;
    --gold-light: #e9bd3c;
    --ink: #1c1c1c;
    --navy: #0b3157;
    --navy-deep: #072442;
    --white: #ffffff;
    --leather: #c89f78;
    --fur: #6b4a33;
    --stone: #7d7a73;
  }
  * { box-sizing: border-box; margin: 0; padding: 0; }
  html, body { width: 963px; height: 1200px; overflow: hidden; }
  body { background: var(--backdrop); position: relative; }

  .card {
    position: absolute; top: 288px; width: 440px; height: 623px;
    box-shadow: 0 3px 8px rgba(0,0,0,.25);
    overflow: hidden;
  }
  .card__frame { position: absolute; inset: 0; width: 100%; height: 100%; fill: none; stroke-width: 1.4; }

  /* Front */
  .card--front {
    left: 30px;
    background: radial-gradient(ellipse at 50% 45%, var(--sky-light) 0%, var(--sky) 75%);
  }
  .card--front .card__frame { stroke: var(--ink); }
  .brand { position: absolute; left: 0; right: 0; display: flex; align-items: center; justify-content: center; gap: 10px; }
  .brand__dot { width: 34px; height: 34px; border-radius: 50%; }
  .brand__name { font-family: "Quicksand", sans-serif; font-weight: 700; font-size: 22px; letter-spacing: .5px; }
  .card--front .brand { top: 62px; }
  .card--front .brand__dot { background: var(--gold-light); }
  .card--front .brand__name { color: var(--gold); }

  .hero-chair {
    position: absolute; left: 120px; top: 150px; width: 200px; height: 260px;
    background: radial-gradient(ellipse at 50% 38%, var(--fur) 0%, var(--leather) 48%, rgba(200,159,120,0) 70%);
  }
  .product-title {
    position: absolute; top: 430px; left: 0; right: 0; text-align: center;
    font-family: "Quicksand", sans-serif; font-weight: 700; font-size: 37px;
    color: var(--gold); letter-spacing: 1px;
  }
  .product-blurb {
    position: absolute; top: 494px; left: 40px; right: 40px; text-align: center;
    font-family: "Patrick Hand", cursive; font-size: 15.5px; line-height: 18.5px; color: var(--ink);
  }

  /* Back */
  .card--back {
    left: 493px;
    background: linear-gradient(180deg, var(--navy) 0%, var(--navy-deep) 100%);
    color: var(--white);
    font-family: "Open Sans", sans-serif;
  }
  .card--back .card__frame { stroke: var(--white); }
  .card--back .brand { top: 50px; flex-direction: column; gap: 8px; }
  .card--back .brand__dot { width: 70px; height: 70px; background: var(--white); }
  .card--back .brand__name { color: var(--white); font-size: 22px; }

  .features { position: absolute; left: 26px; top: 172px; width: 250px; }
  .features__title { font-weight: 600; font-size: 16px; margin-bottom: 8px; }
  .features__list { list-style: none; font-size: 11.5px; line-height: 18.5px; }
  .features__list li { display: flex; align-items: center; gap: 9px; }
  .features__list svg { width: 10px; height: 10px; stroke: var(--white); fill: none; stroke-width: 1.6; flex: none; }

  .photo { position: absolute; border: 3px solid var(--white); }
  .photo--fireplace {
    left: 282px; top: 180px; width: 140px; height: 175px;
    background: linear-gradient(90deg, var(--stone) 0%, #5a5751 55%, #b8a89a 100%);
  }
  .photo--room {
    left: 34px; top: 388px; width: 133px; height: 178px;
    background: linear-gradient(160deg, #8a8680 0%, #d5d0c8 45%, var(--leather) 100%);
  }
  .photo-bracket { position: absolute; border-color: var(--white); border-style: solid; width: 40px; height: 40px; }
  .photo-bracket--tl { left: 263px; top: 173px; border-width: 2px 0 0 2px; }
  .photo-bracket--br { left: 392px; top: 338px; border-width: 0 2px 2px 0; }
  .photo-bracket--room { left: 30px; top: 383px; border-width: 2px 0 0 2px; }

  .about {
    position: absolute; right: 26px; top: 413px; width: 245px; text-align: right;
    font-size: 8.8px; line-height: 10.4px;
  }
  .about__brand { font-weight: 600; font-size: 14px; line-height: 17px; }
  .about p { margin-bottom: 6px; }
  .contact { list-style: none; margin-top: 4px; }
  .contact li { display: flex; justify-content: flex-end; align-items: center; gap: 8px; line-height: 14.5px; }
  .contact svg { width: 8px; height: 8px; fill: none; stroke: var(--white); stroke-width: 1.2; }
</style>
</head>
<body>

<section class="card card--front" aria-label="Front of card">
  <svg class="card__frame" viewBox="0 0 440 623" aria-hidden="true">
    <path d="M28 16 H412 A12 12 0 0 0 424 28 V595 A12 12 0 0 0 412 607 H28 A12 12 0 0 0 16 595 V28 A12 12 0 0 0 28 16 Z"/>
  </svg>
  <div class="brand">
    <span class="brand__dot"></span>
    <span class="brand__name">TRV UNIQUE PRODUCTS</span>
  </div>
  <div class="hero-chair" role="img" aria-label="Leather dome chair lined with brown sheepskin on a round wooden base"></div>
  <h1 class="product-title">BURROW CHAIR</h1>
  <p class="product-blurb">This chair is unique and a labor of love and attention to detail, it's a conversation starter or statement piece. It's something you just cant find anywhere.<br>The acoustics let you escape in any room whether you want to read a book or simply relax</p>
</section>

<section class="card card--back" aria-label="Back of card">
  <svg class="card__frame" viewBox="0 0 440 623" aria-hidden="true">
    <path d="M28 16 H412 A12 12 0 0 0 424 28 V595 A12 12 0 0 0 412 607 H28 A12 12 0 0 0 16 595 V28 A12 12 0 0 0 28 16 Z"/>
  </svg>
  <div class="brand">
    <span class="brand__dot"></span>
    <span class="brand__name">TRV UNIQUE PRODUCTS</span>
  </div>

  <div class="features">
    <h2 class="features__title">The Dome or Halo chair</h2>
    <ul class="features__list">
      <li><svg viewBox="0 0 10 10"><path d="M1 5.5 L4 8.5 L9 1.5"/></svg>Upholstered in Italian Leather</li>
      <li><svg viewBox="0 0 10 10"><path d="M1 5.5 L4 8.5 L9 1.5"/></svg>High Quality Merino Wool Sheepskins.</li>
      <li><svg viewBox="0 0 10 10"><path d="M1 5.5 L4 8.5 L9 1.5"/></svg>360 Degree rotation</li>
      <li><svg viewBox="0 0 10 10"><path d="M1 5.5 L4 8.5 L9 1.5"/></svg>Handmade with love and detail</li>
      <li><svg viewBox="0 0 10 10"><path d="M1 5.5 L4 8.5 L9 1.5"/></svg>Cosy</li>
      <li><svg viewBox="0 0 10 10"><path d="M1 5.5 L4 8.5 L9 1.5"/></svg>Calming and unbelievably quiet acoustics</li>
      <li><svg viewBox="0 0 10 10"><path d="M1 5.5 L4 8.5 L9 1.5"/></svg>Unique</li>
    </ul>
  </div>

  <span class="photo-bracket photo-bracket--tl"></span>
  <span class="photo-bracket photo-bracket--br"></span>
  <div class="photo photo--fireplace" role="img" aria-label="Dome chair beside a stacked stone fireplace"></div>

  <span class="photo-bracket photo-bracket--room"></span>
  <div class="photo photo--room" role="img" aria-label="Dome chair in a bright living room next to a stone fireplace"></div>

  <div class="about">
    <p>We are a small Australian Family creating unique products<br><span class="about__brand">TRV</span><br>Property of TRV Exports we love to create comfortable and unique things which people talk about and want to adorn their living spaces with.</p>
    <p>We hope you love this product as much as we do and have many years enjoyment in it Please order on our web site</p>
    <p>Mira Doyle<br>Marketing and Sales Manager</p>
    <ul class="contact">
      <li><svg viewBox="0 0 8 8"><path d="M2 1 L3 3 L2.5 4 Q3.5 5.5 4 5.5 L5 5 L7 6 L6 7.5 Q1 6.5 0.5 1.5 Z"/></svg>0491 203 417</li>
      <li><svg viewBox="0 0 8 8"><rect x="0.5" y="1.5" width="7" height="5"/><path d="M0.5 1.5 L4 4.5 L7.5 1.5"/></svg>sales@trvexp-example.com.au</li>
      <li><svg viewBox="0 0 8 8"><circle cx="4" cy="4" r="3.4"/><path d="M0.6 4 H7.4 M4 0.6 V7.4"/></svg>www.trvexports-example.com.au</li>
      <li>Melbourne, Australia</li>
    </ul>
  </div>
</section>

</body>
</html>
```